Letterhead to Prospective Clients

Create a letterhead (word & canva) that I will use to send letters to prospective clients and also include the Coralwood Estate Partners Logo, My Contact Details and Interchangeable "Suburb". Use the same font and colour pallete

Maris Dulworth | "Suburb" Specialist - Redlands & Surrounds
Mobile: 0417 862 095
Email: MD@CoralwoodEstatePartners.com.au

```html
<!DOCTYPE html>
<html lang="en">
<head>
<meta charset="utf-8">
<title>Coralwood Estate Partners – Letterhead</title>
<link rel="stylesheet" href="https://fonts.googleapis.com/css2?family=Arimo:wght@400&display=swap">
<style>
  :root {
    --backdrop: #e4e6e9;
    --paper: #ffffff;
    --navy: #0c1a3d;
    --on-navy: #ffffff;
  }
  html, body {
    margin: 0;
    padding: 0;
    width: 1200px;
    height: 1200px;
    overflow: hidden;
    background: var(--backdrop);
    font-family: "Arimo", Arial, sans-serif;
  }
  .letterhead {
    position: absolute;
    left: 241px;
    top: 93px;
    width: 717px;
    height: 1014px;
    background: var(--paper);
    overflow: hidden;
  }
  .brand-name {
    position: absolute;
    left: 56px;
    top: 158px;
    margin: 0;
    font-size: 27px;
    font-weight: 400;
    letter-spacing: 3px;
    text-transform: uppercase;
    color: var(--navy);
    white-space: nowrap;
  }
  .footer-wave {
    position: absolute;
    left: 0;
    top: 0;
    width: 717px;
    height: 1014px;
  }
  .footer-wave path { fill: var(--navy); }
  .agent-details {
    position: absolute;
    left: 57px;
    top: 918px;
    color: var(--on-navy);
  }
  .agent-name {
    margin: 0;
    font-size: 18px;
    font-weight: 400;
    line-height: 22px;
  }
  .agent-role {
    margin: 2px 0 0;
    font-size: 11px;
    line-height: 14px;
  }
  .agent-contact {
    margin: 14px 0 0;
    font-size: 11px;
    line-height: 14px;
    white-space: nowrap;
  }
  .agent-contact .divider { margin: 0 12px; }
</style>
</head>
<body>
  <main class="letterhead">
    <p class="brand-name">Coralwood Estate Partners</p>

    <svg class="footer-wave" viewBox="0 0 717 1014" aria-hidden="true">
      <path d="M0 919 C 40 908, 80 900, 130 900 C 330 900, 470 990, 600 986 C 650 984, 690 972, 717 964 L 717 1014 L 0 1014 Z"/>
    </svg>

    <section class="agent-details">
      <p class="agent-name">Maris Dulworth</p>
      <p class="agent-role">"Suburb" Specialist - Redlands &amp; Surrounds</p>
      <p class="agent-contact">M: 0417 862 095<span class="divider">|</span>E: MD@CoralwoodEstatePartners.com.au</p>
    </section>
  </main>
</body>
</html>
```